Postcard Design Project

script called Lanterns Over Quiet Harbor Road based on a true story and a book by the same author. It needs to have the Marlowe Creek Cinema Showcase logo and my contact info. dorothea.quillan@pellimoremail.org and phone: 555-014-7291, the logline and the synopsis on the back of the card. Below my photo: Dorothea Quillan is a script writer with shares in two Harcastle Medals, a published book, a Pellimore and other awards. Should have a large headline over the booking photo: Lanterns Over Quiet Harbor Road, feature film/drama based on a true story
Updates

I don't see where you added my web site. It should be on the front by the phone. www.dorotheaquillan.com

Target Market(s)

producers and agents looking for scripts

Industry/Entity Type

Movie Production

Font styles to use
Serif

Requirements
Must have
• www.dorotheaquillan.com dorothea.quillan@pellimoremail.org
• logline (included in the file attached), photo of the boy, author biographical infor., contact information and web site. Marlowe creek Cinema Showcase logo can be downloaded from http://marlowecreekshowcase.com/entry-rules/ I need the logo that says "official selection" at the top
Nice to have
• head shot of the author, dorothea quillan

```html
<!DOCTYPE html>
<html lang="en">
<head>
<meta charset="utf-8">
<title>Lanterns Over Quiet Harbor Road – Postcard</title>
<link rel="stylesheet" href="https://fonts.googleapis.com/css2?family=Oswald:wght@500;600&family=Lato:wght@400;700;900&display=swap">
<style>
  :root{
    --page:#dcdcdc;
    --ink-dark:#151515;
    --gold:#c9962e;
    --gold-light:#f0c862;
    --paper:#ece9e6;
    --white:#ffffff;
    --text-light:#e8e8e8;
    --text-name:#2a1c05;
  }
  *{box-sizing:border-box;margin:0;padding:0}
  html,body{width:902px;height:1200px;overflow:hidden}
  body{background:var(--page);font-family:'Lato',sans-serif;position:relative}

  .card{position:absolute;width:709px;height:480px;overflow:hidden;box-shadow:0 8px 14px rgba(0,0,0,.35)}
  .card-front{left:75px;top:100px;background:var(--paper)}
  .card-back{left:143px;top:622px;background:linear-gradient(135deg,#2a2a2a,#141414 70%)}
  .card svg.shapes{position:absolute;inset:0}

  .festival-name{position:absolute;font-family:'Lato',sans-serif;font-weight:900;color:var(--white);text-transform:uppercase;line-height:1.1;letter-spacing:.3px;white-space:nowrap}
  .festival-dates{position:absolute;font-size:6.5px;color:var(--white);letter-spacing:1px;white-space:nowrap}
  .front-festival{left:128px;top:56px;font-size:12px}
  .front-dates{left:128px;top:86px}
  .back-festival{left:568px;top:32px;font-size:10px}
  .back-dates{left:568px;top:58px;font-size:5.5px}

  .headline{position:absolute;left:274px;top:52px;font-family:'Oswald',sans-serif;color:var(--white);text-transform:uppercase;line-height:1.2;white-space:nowrap}
  .headline .title{display:block;font-size:27px;font-weight:600}
  .headline .tag{display:block;font-size:23px;font-weight:500}

  .photo-slot{position:absolute;background:linear-gradient(135deg,#5a5a5a,#1e1e1e)}
  .boy-photo{left:266px;top:173px;width:419px;height:224px;border:3px solid #1a1a1a}
  .author-photo{border-radius:50%;border:4px solid var(--white);background:radial-gradient(circle at 50% 45%,#b07a55,#5a3a22)}
  .front-author{left:40px;top:190px;width:142px;height:142px}
  .back-author{left:603px;top:258px;width:102px;height:102px}

  .contact{position:absolute;color:var(--ink-dark)}
  .front-contact{left:48px;top:384px}
  .front-contact .name{font-size:16px;font-weight:700;text-transform:uppercase;letter-spacing:.5px;margin-bottom:8px;color:var(--text-name)}
  .contact .row{display:flex;align-items:center;gap:6px;font-weight:700;white-space:nowrap}
  .front-contact .phone{font-size:16px;margin-bottom:4px}
  .front-contact .web,.front-contact .mail{font-size:11px;margin-bottom:3px}
  .icon{width:11px;height:11px;flex:none}

  .site{position:absolute;color:var(--white);font-size:15px;font-weight:700;letter-spacing:1.2px;display:flex;align-items:center;gap:10px;white-space:nowrap}
  .front-site{left:335px;top:450px}
  .back-site{left:118px;top:462px;font-size:13px}
  .site .icon{width:10px;height:10px}

  .copy{position:absolute;left:20px;top:20px;width:650px;color:var(--text-light);font-size:8.6px;line-height:1.2}
  .copy h2{font-size:15px;font-weight:700;color:var(--gold-light);margin-bottom:3px}
  .copy .logline{width:490px;margin-bottom:6px}
  .copy .logline b{color:var(--gold-light);font-weight:400}
  .copy p{margin-bottom:4px}
  .copy .narrow{width:570px}
  .copy .narrower{width:520px}

  .back-contact{left:530px;top:368px;width:170px;text-align:right;color:var(--ink-dark)}
  .back-contact .name{font-size:12px;font-weight:900;text-transform:uppercase;margin-bottom:3px}
  .back-contact .bio{font-size:7px;font-style:italic;line-height:1.3;margin-bottom:8px}
  .back-contact .row{justify-content:flex-end;font-size:8.5px;margin-bottom:2px}
  .back-contact .phone{font-size:10px}
  .back-contact .icon{width:8px;height:8px}
</style>
</head>
<body>

<section class="card card-front">
  <svg class="shapes" width="709" height="480" viewBox="0 0 709 480">
    <defs>
      <linearGradient id="gold-front" x1="0" y1="0" x2="1" y2="1">
        <stop offset="0" stop-color="#f2cd68"/><stop offset=".5" stop-color="#c9962e"/><stop offset="1" stop-color="#8a6216"/>
      </linearGradient>
      <linearGradient id="stage-tone" x1="0" y1="0" x2="0" y2="1">
        <stop offset="0" stop-color="#5a1d1a"/><stop offset=".6" stop-color="#241010"/><stop offset="1" stop-color="#0c0c0c"/>
      </linearGradient>
    </defs>
    <rect class="top-band" x="0" y="0" width="709" height="128" fill="url(#stage-tone)" role="img" aria-label="Cinema seats in a darkened theatre"/>
    <rect class="gold-rule" x="0" y="128" width="709" height="7" fill="url(#gold-front)"/>
    <rect class="bottom-band" x="0" y="418" width="709" height="62" fill="#0c0c0c"/>
    <path class="gold-panel-edge" d="M0,0 H135 C110,80 95,170 120,240 C150,320 240,380 278,480 H0 Z" fill="#d9d9d9"/>
    <path class="gold-panel" d="M0,0 H125 C100,80 86,170 110,240 C140,320 228,380 266,480 H0 Z" fill="url(#gold-front)"/>
  </svg>

  <div class="festival-name front-festival">Marlowe Creek<br>Cinema Showcase</div>
  <div class="festival-dates front-dates">APRIL 26–30, 2017</div>

  <h1 class="headline">
    <span class="title">Lanterns Over Quiet Harbor Road,</span>
    <span class="tag">Feature film/drama based on a true</span>
  </h1>

  <div class="photo-slot boy-photo" role="img" aria-label="Archival black and white booking photo of a young boy, profile and front views"></div>
  <div class="photo-slot author-photo front-author" role="img" aria-label="Head shot of author Dorothea Quillan"></div>

  <div class="contact front-contact">
    <div class="name">Dorothea Quillan</div>
    <div class="row phone">
      <svg class="icon" viewBox="0 0 12 12"><circle cx="6" cy="6" r="5.3" fill="none" stroke="#151515" stroke-width="1"/><path d="M4 3.2l1 .1.5 1.4-.7.6c.4.8 1 1.4 1.8 1.8l.6-.7 1.4.5.1 1c-.3.5-.8.7-1.3.6C5.3 8.2 3.8 6.7 3.5 4.6c-.1-.6.1-1.1.5-1.4z" fill="#151515"/></svg>
      555-014-7291
    </div>
    <div class="row web">
      <svg class="icon" viewBox="0 0 12 12"><circle cx="6" cy="6" r="5" fill="none" stroke="#151515"/><ellipse cx="6" cy="6" rx="2.2" ry="5" fill="none" stroke="#151515"/><path d="M1 6h10" stroke="#151515"/></svg>
      www.dorotheaquillan.com
    </div>
    <div class="row mail">
      <svg class="icon" viewBox="0 0 12 12"><rect x="1" y="2.5" width="10" height="7" fill="none" stroke="#151515"/><path d="M1 2.5l5 4 5-4" fill="none" stroke="#151515"/></svg>
      dorothea.quillan@pellimoremail.org
    </div>
  </div>

  <div class="site front-site">
    <svg class="icon" viewBox="0 0 12 12"><circle cx="6" cy="6" r="5" fill="none" stroke="#c9962e" stroke-width="1.4"/><path d="M1 6h10M6 1v10" stroke="#c9962e"/></svg>
    www.marlowecreekshowcase.com
  </div>
</section>

<section class="card card-back">
  <svg class="shapes" width="709" height="480" viewBox="0 0 709 480">
    <defs>
      <linearGradient id="gold-back" x1="1" y1="0" x2="0" y2="1">
        <stop offset="0" stop-color="#f2cd68"/><stop offset=".55" stop-color="#c9962e"/><stop offset="1" stop-color="#8a6216"/>
      </linearGradient>
    </defs>
    <path class="gold-panel-edge" d="M650,0 H709 V480 H515 C560,400 600,330 690,240 C720,170 700,60 650,0 Z" fill="#d9d9d9"/>
    <path class="gold-panel" d="M662,0 H709 V480 H527 C572,400 612,335 700,246 C728,170 712,60 662,0 Z" fill="url(#gold-back)"/>
    <path class="bottom-band" d="M0,440 H540 C535,455 530,468 527,480 H0 Z" fill="#0a0a0a"/>
  </svg>

  <div class="festival-name back-festival">Marlowe Creek<br>Cinema Showcase</div>
  <div class="festival-dates back-dates">APRIL 26–30, 2017</div>

  <div class="copy">
    <h2>Feature film/drama</h2>
    <p class="logline"><b>Logline:</b> In 1931, a 60-pound 12-year-old boy is sentenced to life in prison for murder. In this true story based on a book, the boy must learn how to navigate deadly politics amidst dangerous men and decide if becoming a savage is the way to become a man.</p>
    <h2>Synopsis</h2>
    <p>In this 1931 true story 12-year-old Henry Nolan runs away from his abusive grandmother, breaks into the general store to get something to eat and is surprised in the act by the sheriff. Henry fires a gun, accidentally kills the sheriff and is sentenced to life in an adult prison. He brings with him a beautiful blue marble, a souvenir of the summer skies of his childhood.</p>
    <p>As soon as Henry gets to prison the power-hungry Guard Smedley puts him in a cell with Blu, an insane, homicidal pedophile. But Ray, a cunning con, comes to the naive boy's aid. The no-nonsense Warden McCauley assigns Henry to share a cell with Walter, a sullen 17-year-old, who becomes Henry's closest friend. Ray continues to do Henry favors and Walter cautions Henry that Ray is not to be trusted.</p>
    <p>Hollow Pines Home's Father Corrigan and a Seattle society woman, Adele Lawson, in the meantime, campaign to parole Henry to Hollow Pines Home, irritating the autocrat, Gov. Edwin Marsh, who will do anything to keep the boy in prison as a symbol of being tough on crime.</p>
    <p class="narrow">In the meantime, Ray decides it is time to collect on the favors he has given to Henry. Ray plans to escape and needs Henry's help. Henry agrees but when he realizes what he is asked to do will kill his friend, the prison librarian, he changes his mind. Just before the librarian drinks poison, Henry knocks the cup away and blames Ray. Ray and his friends wait to get Henry alone and plan to rape him.</p>
    <p class="narrow">Walter hears Henry scream and with mad-dog viciousness, Walter attacks Ray and his friends, killing one. Walter is sentenced to be executed and on the night of the hanging, Henry escapes from his cell to try to save him. Henry pleads with the warden to spare Walter and admits that had he not first agreed to poison the librarian, the trouble with Ray would never have started.</p>
    <p class="narrow">McCauley is upset and continues the execution as Henry watches the brutal scene and changes from compliant to vicious and rebellious. Smedley takes Henry to solitary and beats him. The next day, McCauley, a by-the-rules warden who is often at odds with Smedley, confronts the guard and orders him to report to his office. Instead, the guard retaliates by freeing a cellblock full of prisoners and a riot begins. Guards are taken hostage as prisoners try to escape. Ray is looking for Henry and just as he comes close, McCauley steps into Ray's path, sacrificing himself to become Ray's hostage but saving the boy. Henry sees the door to the sally port open and sees prisoners running to freedom. He begins to run until he sees McCauley lying wounded and calling him for help. But helping means confronting Ray and with mad-dog viciousness, Henry fights Ray, killing him. Henry turns to McCauley and tries to help him. By doing so he gives up his chance for freedom and the gates close out the light. Lawson, Corrigan, McCauley and Henry gather at the parole board hearing. Gov. Marsh stamps papers. He rejects Henry's parole. Afterward, a tearful Lawson vows to continue the fight.</p>
    <p class="narrower">Nine years after Henry first entered prison, he is released and will go on to lead a crime-free life and work for Meridian Pictures, but as he says, “Like the once beautiful blue marble, what goes into prison comes out broken.”</p>
  </div>

  <div class="photo-slot author-photo back-author" role="img" aria-label="Head shot of author Dorothea Quillan"></div>

  <div class="contact back-contact">
    <div class="name">Dorothea Quillan</div>
    <div class="bio">Script writer with shares in two<br>Harcastle Medals, a published book,<br>a Pellimore and other awards</div>
    <div class="row phone">555-014-7291
      <svg class="icon" viewBox="0 0 12 12"><circle cx="6" cy="6" r="5" fill="none" stroke="#fff" stroke-width="1.4"/></svg>
    </div>
    <div class="row">www.dorotheaquillan.com
      <svg class="icon" viewBox="0 0 12 12"><circle cx="6" cy="6" r="5" fill="#fff"/></svg>
    </div>
    <div class="row">dorothea.quillan@pellimoremail.org
      <svg class="icon" viewBox="0 0 12 12"><rect x="1" y="2.5" width="10" height="7" fill="#fff"/></svg>
    </div>
  </div>

  <div class="site back-site">
    <svg class="icon" viewBox="0 0 12 12"><circle cx="6" cy="6" r="5" fill="none" stroke="#c9962e" stroke-width="1.4"/><path d="M1 6h10M6 1v10" stroke="#c9962e"/></svg>
    www.marlowecreekshowcase.com
  </div>
</section>

</body>
</html>
```